Harbin Cargo needs a business card design.

Design a double-sided business card for new freight business. On the front, would like to see our logo along with the following info:

Nathaniel Voskuhl
CEO/FOUNDER
617-552-0194
nathanielvoskuhl@harbin-cargo.example

On the reverse side, we would like to use the graphic image of our logo only without the Harbin Cargo name.

```html
<!DOCTYPE html>
<html lang="en">
<head>
<meta charset="utf-8">
<title>Harbin Cargo – Business Card</title>
<link rel="stylesheet" href="https://fonts.googleapis.com/css2?family=Poppins:wght@400;500;700&display=swap">
<style>
  :root {
    --navy: #1c1a5c;
    --red: #c0202c;
    --white: #ffffff;
    --stage: #e9e7e3;
    --ink: #1e1d3f;
    --pattern-light: #f8f8f8;
    --pattern-mid: #ececec;
  }
  * { margin: 0; padding: 0; box-sizing: border-box; }
  html, body {
    width: 1200px; height: 900px; overflow: hidden;
    background: var(--stage);
    font-family: "Poppins", sans-serif;
  }
  .sheet {
    width: 1200px; height: 900px;
    display: flex; flex-direction: column;
    align-items: center; justify-content: center; gap: 56px;
  }
  .card {
    position: relative;
    width: 600px; height: 343px;
    background: var(--white);
    border-radius: 18px;
    overflow: hidden;
    box-shadow: 0 6px 18px rgba(0,0,0,0.12);
  }

  /* Front */
  .wordmark {
    position: absolute; left: 40px; top: 34px;
    display: flex; align-items: center; gap: 24px;
  }
  .wordmark-square { width: 92px; height: 92px; background: var(--navy); flex: none; }
  .wordmark-name {
    font-weight: 700; font-size: 50px; letter-spacing: 6px;
    color: var(--navy); text-transform: uppercase; line-height: 1.02;
  }
  .contact-row {
    position: absolute; left: 40px; top: 178px;
    display: flex; align-items: center; gap: 16px;
  }
  .identity { text-align: right; }
  .person-name { font-weight: 700; font-size: 15px; color: var(--navy); }
  .person-title { font-weight: 400; font-size: 14px; color: var(--red); letter-spacing: 0.5px; }
  .divider { width: 2px; height: 48px; background: var(--red); }
  .details { display: flex; flex-direction: column; gap: 5px; }
  .detail { display: flex; align-items: center; gap: 8px; font-size: 14px; color: var(--ink); white-space: nowrap; }
  .detail svg { width: 13px; height: 13px; flex: none; }
  .band-stripe { position: absolute; left: 0; right: 0; bottom: 62px; height: 5px; background: var(--red); }
  .band { position: absolute; left: 0; right: 0; bottom: 0; height: 62px; background: var(--navy); }

  /* Back */
  .back-pattern {
    position: absolute; inset: 0;
    background: linear-gradient(135deg, var(--pattern-light), var(--pattern-mid) 50%, var(--pattern-light));
  }
  .back-mark {
    position: absolute; left: 50%; top: 50%; transform: translate(-50%, -50%);
    width: 44px; height: 44px; background: var(--navy);
  }
</style>
</head>
<body>
<main class="sheet">
  <section class="card card-front" aria-label="Business card front">
    <div class="wordmark">
      <span class="wordmark-square"></span>
      <span class="wordmark-name">Harbin<br>Cargo</span>
    </div>
    <div class="contact-row">
      <div class="identity">
        <p class="person-name">Nathaniel Voskuhl</p>
        <p class="person-title">CEO/FOUNDER</p>
      </div>
      <span class="divider"></span>
      <div class="details">
        <p class="detail">
          <svg viewBox="0 0 16 16" aria-hidden="true"><path fill="#c0202c" d="M3.5 1.5l2.5 0 1 3.5-1.6 1.2a8 8 0 0 0 4.4 4.4L11 9l3.5 1v2.5c0 1-1 2-2 2C6.7 14.5 1.5 9.3 1.5 3.5c0-1 1-2 2-2z"/></svg>
          617-552-0194
        </p>
        <p class="detail">
          <svg viewBox="0 0 16 16" aria-hidden="true"><rect x="1" y="3" width="14" height="10" fill="#c0202c"/><path d="M1.5 3.5L8 9l6.5-5.5" fill="none" stroke="#fff" stroke-width="1.4"/></svg>
          nathanielvoskuhl@harbin-cargo.example
        </p>
      </div>
    </div>
    <div class="band-stripe"></div>
    <div class="band"></div>
  </section>

  <section class="card card-back" aria-label="Business card back">
    <div class="back-pattern" role="img" aria-label="Faint repeating brand pattern in light grey"></div>
    <span class="back-mark" aria-hidden="true"></span>
  </section>
</main>
</body>
</html>
```